Cartlyft product design and upload for Coffee Shop

Coffee Shop, Store Front & Online - Cartlyft theme

***Important*** Credentials to complete the gig will only be shared via Keyvaultly or a similar password share application. Please ensure you will be able to do this before proceeding.

Please advise if you have worked with any Cartlyft theme in storewell?

Job Description
Set up and customize all products to Storewell for my Coffee Shop and customize to my colours and brand - using the current installed cartlyft theme.

Hi there, I have a "Physical retail Cafe" I am looking for someone to upload the attached menu for me in the products section of my Storewell store and make the store look and display awesome. Need expert who has a good understanding of the storewell and cartlyft system as I need a quick turn around.

Existing Old site - www.mugamiles.com.au
New storewell site to be set up with cartlyft theme - https://mugamiles.mystorewell.com/

Attached in these excel spreadsheets are the menus:
1.Muga Miles Insotre Menu - Muga Miles Online Shop Menu
2. Muga Miles Online Shop Menu

1. In Store Menu - where customers can only purchase the items in the store - however they will be able to view all items online. So a visually appealing display of products and ease of viewing of the menu is important.
Currently customers can order this menu here - http://tapvia.example/r82kzm using phone app, computer or any device and pick up only from store.

2. Online Shop Menu - They can purchase these items online and we can ship.

Examples provided below of how I would like the sites I like - and would like similar design using our products and items. Please feel free to use your expertise to solve and issues or improve.
Also I am happy to discuss any ideas or questions you have.

We do not have many images of our products at the moment so please free to use any of the images from below sites as a temporary pic - unless you can source some better original ones or have some ideas...

Please see all attachments for full details.

Target Market(s)

Coffee Shop - Retail Store Front & Online

Colors
fffefc
ffffff

Requirements
Must have
• Pleas read attached brief
Nice to have
• Experience using cartlyft theme. Open to using another theme if designer can deisgn style I am looking for as per the examples in the brief.
Should not have
• As per the brieft

```html
<!DOCTYPE html>
<html lang="en">
<head>
<meta charset="utf-8">
<title>Muga Miles – Daily Fresh Coffee</title>
<link href="https://fonts.googleapis.com/css2?family=Poppins:wght@400;500&family=Montserrat:wght@400;500&family=Yesteryear&family=Lemon&family=Roboto:wght@400&display=swap" rel="stylesheet">
<style>
  :root{
    --hero-dark:#3b1d10;
    --hero-mid:#b9683d;
    --hero-deep:#7b321d;
    --white:#ffffff;
    --paper:#fffefc;
    --button:#bf9f7a;
    --title:#4a2f2b;
    --accent:#8b3a28;
    --body:#222222;
    --icon:#8b4a38;
    --brand-red:#c8202f;
    --cup-light:#f1ece6;
    --cup-sleeve:#c9b29a;
  }
  *{margin:0;padding:0;box-sizing:border-box}
  html,body{width:1200px;height:986px;overflow:hidden;background:var(--white)}
  body{position:relative;font-family:'Roboto',sans-serif}
  .hero{position:absolute;left:0;top:0;width:1200px;height:508px;
    background:
      radial-gradient(ellipse 420px 380px at 380px 260px, rgba(214,150,110,.55), rgba(0,0,0,0) 70%),
      linear-gradient(90deg,var(--hero-dark) 0%,#6a3620 18%,var(--hero-mid) 52%,#a9522e 78%,var(--hero-deep) 100%);}
  .brand{position:absolute;left:79px;top:8px;width:76px;height:76px;border-radius:50%;
    background:var(--brand-red);display:flex;align-items:center;justify-content:center;
    font-family:'Poppins',sans-serif;font-weight:500;font-size:12px;color:var(--white);text-align:center;line-height:1.1}
  .nav{position:absolute;top:34px;left:0;width:1200px;font-family:'Poppins',sans-serif;font-weight:500;font-size:12px;color:var(--white)}
  .nav span{position:absolute;white-space:nowrap;display:flex;align-items:center;gap:4px}
  .caret{width:0;height:0;border-left:3.5px solid transparent;border-right:3.5px solid transparent;border-top:4px solid var(--white)}
  .headline{position:absolute;left:560px;width:484px;top:158px;text-align:center;font-family:'Yesteryear',cursive;font-size:58px;color:var(--white);line-height:1}
  .offer{position:absolute;left:600px;width:404px;top:243px;text-align:center;font-family:'Montserrat',sans-serif;font-weight:500;font-size:30px;letter-spacing:1px;color:var(--white)}
  .buy{position:absolute;left:737px;top:321px;width:133px;height:43px;background:var(--button);color:var(--white);
    font-family:'Montserrat',sans-serif;font-size:15px;display:flex;align-items:center;justify-content:center;letter-spacing:.5px}
  .section-title{position:absolute;top:533px;left:0;width:1200px;text-align:center;font-family:'Lemon',cursive;font-weight:400;font-size:24px;color:var(--title)}
  .feature{position:absolute;width:240px}
  .feature h3{font-family:'Lemon',cursive;font-weight:400;font-size:12.5px;color:var(--accent);margin-bottom:8px;line-height:17px}
  .feature p{font-size:10px;line-height:17px;color:var(--body)}
  .left{left:142px;text-align:right}
  .right{left:818px;text-align:left}
  .icon{position:absolute;width:36px;height:36px}
  .cup-photo{position:absolute;left:500px;top:614px;width:200px;height:326px;border-radius:8px;
    background:linear-gradient(180deg,var(--cup-light) 0%,var(--cup-light) 26%,var(--cup-sleeve) 34%,var(--cup-sleeve) 90%,var(--cup-light) 100%)}
</style>
</head>
<body>
  <div class="hero" role="img" aria-label="Photo of a woman sipping from a white coffee cup against a warm brown backdrop"></div>

  <div class="brand">Muga<br>Miles</div>

  <nav class="nav">
    <span style="left:505px">Home</span>
    <span style="left:558px">Instore Menu <i class="caret"></i></span>
    <span style="left:668px">Shop <i class="caret"></i></span>
    <span style="left:735px">Coffee <i class="caret"></i></span>
    <span style="left:808px">Snacks <i class="caret"></i></span>
    <span style="left:888px">Pages <i class="caret"></i></span>
    <span style="left:972px;top:1px">
      <svg width="13" height="13" viewBox="0 0 13 13"><circle cx="5.3" cy="5.3" r="4" fill="none" stroke="#fff" stroke-width="2"/><line x1="8.3" y1="8.3" x2="12" y2="12" stroke="#fff" stroke-width="2.2" stroke-linecap="round"/></svg>
    </span>
    <span style="left:1008px">AUD <i class="caret"></i></span>
    <span style="left:1069px;top:1px">
      <svg width="12" height="13" viewBox="0 0 12 13"><circle cx="6" cy="3.5" r="3" fill="#fff"/><path d="M0.5 13c0-4 2.5-5.5 5.5-5.5s5.5 1.5 5.5 5.5z" fill="#fff"/></svg>
    </span>
    <span style="left:1102px">
      <svg width="11" height="12" viewBox="0 0 11 12"><path d="M3 4V3a2.5 2.5 0 0 1 5 0v1" fill="none" stroke="#fff" stroke-width="1.4"/><rect x="0.5" y="4" width="10" height="8" rx="1" fill="#fff"/></svg>
      0 items
    </span>
  </nav>

  <div class="headline">Daily Fresh Coffee</div>
  <div class="offer">FLAT 25%OFF</div>
  <div class="buy">BUY NOW</div>

  <h2 class="section-title">Coffee Build Your Base</h2>

  <div class="feature left" style="top:602px"><h3>Croissant</h3><p>Alienum phaedrum torquatos nec eu, vis detraxit<br>periculis ex, nihil expetelis in mei. Meianpe icula<br>euripidis,partem.</p></div>
  <div class="feature left" style="top:718px"><h3>French Toast</h3><p>Alienum phaedrum torquatos nec eu, vis detraxit<br>periculis ex, nihil expetelis in mei. Meianpe icula<br>euripidis,partem.</p></div>
  <div class="feature left" style="top:834px"><h3>Pancakes</h3><p>Alienum phaedrum torquatos nec eu, vis detraxit<br>periculis ex, nihil expetelis in mei. Meianpe icula<br>euripidis,partem.</p></div>

  <div class="feature right" style="top:602px"><h3>Turkish Coffee</h3><p>Alienum phaedrum torquatos nec eu, vis detraxit<br>periculis ex, nihil expetelis in mei. Meianpe icula<br>euripidis,partem.</p></div>
  <div class="feature right" style="top:718px"><h3>Coffee To Go</h3><p>Alienum phaedrum torquatos nec eu, vis detraxit<br>periculis ex, nihil expetelis in mei. Meianpe icula<br>euripidis,partem.</p></div>
  <div class="feature right" style="top:834px"><h3>Morning Coffee</h3><p>Alienum phaedrum torquatos nec eu, vis detraxit<br>periculis ex, nihil expetelis in mei. Meianpe icula<br>euripidis,partem.</p></div>

  <svg class="icon" style="left:408px;top:604px" viewBox="0 0 36 36" fill="none" stroke="var(--icon)" stroke-width="1.4">
    <ellipse cx="11" cy="11" rx="6" ry="8" transform="rotate(-35 11 11)"/><path d="M7 6c3 3 5 7 8 10"/>
    <ellipse cx="23" cy="24" rx="6" ry="8" transform="rotate(35 23 24)"/><path d="M27 19c-3 3-5 7-8 10"/>
  </svg>
  <svg class="icon" style="left:408px;top:720px" viewBox="0 0 36 36" fill="none" stroke="var(--icon)" stroke-width="1.4">
    <path d="M14 3c-2 2 2 3 0 6M18 3c-2 2 2 3 0 6"/><path d="M6 14h22v6a10 10 0 0 1-20 0z"/><path d="M28 16h2a3 3 0 0 1 0 6h-3"/><path d="M5 31h26"/>
  </svg>
  <svg class="icon" style="left:408px;top:836px" viewBox="0 0 36 36" fill="none" stroke="var(--icon)" stroke-width="1.4">
    <path d="M9 10h16l-2 22H11z"/><path d="M9 16h16"/><path d="M20 10l4-8h4"/><circle cx="15" cy="22" r="2"/><circle cx="19" cy="26" r="2"/>
  </svg>
  <svg class="icon" style="left:756px;top:604px" viewBox="0 0 36 36" fill="none" stroke="var(--icon)" stroke-width="1.4">
    <path d="M13 2h10l1 6H12z"/><path d="M10 8h16v4H10z"/><path d="M11 12l2 20h10l2-20"/><circle cx="18" cy="20" r="3"/>
  </svg>
  <svg class="icon" style="left:756px;top:720px" viewBox="0 0 36 36" fill="none" stroke="var(--icon)" stroke-width="1.4">
    <path d="M15 2h6v4h-6z"/><path d="M15 6v5l-3 4v17h12V15l-3-4V6"/><ellipse cx="18" cy="23" rx="3" ry="4"/>
  </svg>
  <svg class="icon" style="left:756px;top:836px" viewBox="0 0 36 36" fill="none" stroke="var(--icon)" stroke-width="1.4">
    <path d="M12 4h10l-1 4h-8z"/><path d="M13 8l-3 10h14l-3-10"/><path d="M10 18l3 14h8l3-14"/><path d="M24 10h4v10l-4 2"/><path d="M10 10l-4 2"/>
  </svg>

  <div class="cup-photo" role="img" aria-label="Product photo of a ribbed takeaway coffee cup with white lid and brand sticker"></div>
</body>
</html>
```